Yacht Management in Miami & Ft Lauderdale (2019Q2)

I’m looking for a flyer to leave places for people to get information about my company and what services we offer.
We offer monthly management plans to ensure the vessel is ready to go at a moments notice. This can be as simple as washing once a week, or as involved as washing, waxing, detailing, provisioning, and crew services.
We also offer bespoke customizations; stereos, on board WiFi, and engineering.

Target Market(s)

Yacht and boat owners.

Font styles to use
Sans Serif

Colors
87d0c7
85cae6
85acd3
cedeed
cee9f5
cfeae6
0455a3

Requirements
Must have
• Must have simple attention grabbing, without being obnoxious.
• Prefer a 3in x 5in post card size. other size may be an option.
• Must be front and back.
Nice to have
• Languages: English, Spanish, Russian
• USA flag logo
Should not have
• Should not have a lot of text. Icons and photos are great.

```html
<!DOCTYPE html>
<html lang="en">
<head>
<meta charset="utf-8">
<title>Harbor Crest – Fair &amp; Friendly Yacht Service</title>
<link rel="stylesheet" href="https://fonts.googleapis.com/css2?family=Montserrat:wght@300;400;600;700;800&display=swap">
<style>
  :root {
    --page-grey: #e6e6e6;
    --card-white: #ffffff;
    --brand-red: #ec1c24;
    --ink-black: #111111;
    --sea-deep: #1f4a5c;
    --sea-light: #5f8f9c;
    --inset-tone: #6f7f6a;
  }
  * { box-sizing: border-box; margin: 0; padding: 0; }
  html, body {
    width: 1200px; height: 833px; overflow: hidden;
    background: var(--page-grey);
    font-family: "Montserrat", Arial, sans-serif;
  }
  .flyer {
    position: absolute; left: 50px; top: 50px;
    width: 1101px; height: 732px;
    background: var(--card-white);
    overflow: hidden;
    box-shadow: 6px 8px 10px rgba(0,0,0,0.35);
  }
  .flyer-shapes { position: absolute; inset: 0; }
  .brand-name {
    position: absolute; left: 600px; width: 460px; top: 100px;
    display: flex; align-items: center; justify-content: center; gap: 14px;
    font-weight: 800; font-size: 44px; color: var(--ink-black);
    letter-spacing: 1px;
  }
  .brand-dot { width: 22px; height: 22px; border-radius: 50%; background: var(--ink-black); }
  .headline {
    position: absolute; left: 600px; width: 460px; top: 250px;
    text-align: center; color: var(--card-white); line-height: 1.05;
  }
  .headline-light { display: block; font-weight: 300; font-size: 41px; }
  .headline-bold { display: block; font-weight: 700; font-size: 43px; }
  .services-text {
    position: absolute; left: 600px; width: 460px; top: 366px;
    text-align: center; font-size: 20px; line-height: 25px;
    color: var(--ink-black); font-weight: 400;
  }
  .extras-pill {
    position: absolute; left: 596px; top: 541px; width: 454px; height: 69px;
    background: var(--ink-black); border-radius: 30px;
    text-align: center; padding-top: 9px; line-height: 25px;
  }
  .extras-intro { display: block; color: var(--card-white); font-size: 19px; }
  .extras-list { display: block; color: var(--brand-red); font-size: 18px; font-weight: 700; }
  .contact-line {
    position: absolute; left: 0; width: 1101px; top: 670px;
    text-align: center; font-size: 29px; color: var(--ink-black);
  }
  .contact-line strong { font-weight: 700; color: var(--card-white); }
  .contact-line .contact-phone { color: var(--ink-black); }
</style>
</head>
<body>
<main class="flyer">
  <svg class="flyer-shapes" width="1101" height="732" viewBox="0 0 1101 732" aria-hidden="false">
    <defs>
      <linearGradient id="seaTone" x1="0" y1="0" x2="1" y2="1">
        <stop offset="0" stop-color="var(--sea-light)"/>
        <stop offset="1" stop-color="var(--sea-deep)"/>
      </linearGradient>
    </defs>
    <!-- headline banner -->
    <path d="M560 238 H1101 V349 H575 Z" fill="var(--brand-red)"/>
    <!-- photo edge band -->
    <path d="M0 0 H465 C560 140 600 330 555 500 L540 620 H0 Z" fill="none" stroke="var(--brand-red)" stroke-width="30"/>
    <path d="M0 0 H465 C560 140 600 330 555 500 L540 620 H0 Z" fill="none" stroke="var(--ink-black)" stroke-width="8"/>
    <path d="M0 0 H465 C560 140 600 330 555 500 L540 620 H0 Z" fill="url(#seaTone)" role="img" aria-label="Photo of a motor yacht cruising on open water with a small boat in the distance"/>
    <!-- bottom band -->
    <path d="M540 655 C760 648 980 628 1101 598" fill="none" stroke="var(--ink-black)" stroke-width="8"/>
    <path d="M0 590 C250 560 450 664 700 652 C900 642 1040 615 1101 604 V732 H0 Z" fill="var(--brand-red)"/>
    <!-- inset detail -->
    <circle cx="463" cy="546" r="86" fill="var(--ink-black)"/>
    <circle cx="463" cy="546" r="81" fill="var(--inset-tone)" role="img" aria-label="Close-up photo of an onboard electrical panel with labelled breakers"/>
  </svg>

  <div class="brand-name"><span class="brand-dot"></span>HARBOR CREST</div>

  <h1 class="headline">
    <span class="headline-light">FAIR &amp; FRIENDLY</span>
    <span class="headline-bold">YACHT SERVICE</span>
  </h1>

  <p class="services-text">We offer monthly management plans to ensure the vessel is ready to go at a moments notice. This can be as simple as washing once a week, or as involved as washing, waxing, detailing, provisioning, and crew services.</p>

  <div class="extras-pill">
    <span class="extras-intro">We also offer bespoke customizations;</span>
    <span class="extras-list">Stereos,On board WiFi, and Engineering.</span>
  </div>

  <p class="contact-line">Call us <strong class="contact-phone">(555) 014-2290</strong>&nbsp; or &nbsp;Email us <strong>hello@harborcrest.example</strong></p>
</main>
</body>
</html>
```